I need a SEO-friendly Wordpress website (making sure to style H1, H2, H3, etc correctly) for a Hawaii-based law firm called Meridale Crown Legal Group. Comparable websites include https://brvtlaw.com/ and https://www.lorvin.com/ for design reference. The current copy on the TuvellAttorney.com website can be used.

Coding

Coded - Design and coding required

```html
<!DOCTYPE html>
<html lang="en">
<head>
<meta charset="utf-8">
<title>Meridale Crown Legal Group</title>
<link rel="stylesheet" href="https://fonts.googleapis.com/css2?family=Nunito:wght@800;900&family=Nunito+Sans:wght@300;400;600;700&family=Lato:wght@400;700&display=swap">
<style>
:root{
  --rust:#a4450e;
  --rust-dark:#6e2506;
  --ink:#1f1f1f;
  --muted:#555;
  --line:#d9d9d9;
  --white:#fff;
}
*{box-sizing:border-box;margin:0;padding:0}
html,body{width:1200px;height:2824px;overflow:hidden}
body{position:relative;background:var(--white);font-family:"Nunito Sans",sans-serif;color:var(--ink)}
.abs{position:absolute}
a{color:inherit;text-decoration:none}

/* header */
.site-header{position:absolute;left:0;top:0;width:1200px;height:100px;background:var(--white)}
.brand{left:135px;top:12px}
.brand-name{font-size:22px;line-height:24px;font-weight:600;letter-spacing:.2px;text-transform:uppercase}
.brand-tag{font-size:15px;margin-top:6px;color:#333}
.main-nav{left:445px;top:38px;display:flex;gap:32px;font-size:16px;font-weight:700;text-transform:uppercase}
.phone{left:946px;top:33px;font-size:20px;font-weight:700;display:flex;align-items:center;gap:4px}

/* hero */
.hero{left:0;top:100px;width:1200px;height:650px;background:linear-gradient(180deg,#1c2d62 0%,#2e4c93 30%,#3a5a93 45%,#b5702d 62%,#1f4f8e 80%,#173f78 100%)}
.hero-title{left:0;top:262px;width:1212px;text-align:center;font-family:"Nunito",sans-serif;font-weight:900;font-size:41px;line-height:47px;color:var(--white);text-transform:uppercase;text-shadow:0 2px 6px rgba(0,0,0,.35)}
.btn{display:flex;align-items:center;justify-content:center;background:var(--rust);color:var(--white);font-size:18px;font-weight:600;text-transform:uppercase}
.hero-btn{left:517px;top:425px;width:176px;height:49px}
.slider-dots{left:1051px;top:334px}
.slider-dots span{display:block;width:13px;height:13px;border-radius:50%;background:var(--white);margin-bottom:10px}
.slider-dots span:first-child{background:none;border:2px solid var(--white)}

/* practice areas */
.about-bg{left:0;top:620px;width:1200px;height:650px}
.area{width:270px;height:270px;border-radius:50%;background:var(--white);box-shadow:0 6px 14px rgba(0,0,0,.18);text-align:center;color:#2a2a2a}
.area svg.icon{position:absolute;left:50%;top:50px;transform:translateX(-50%)}
.area-label{position:absolute;left:0;width:100%;top:131px;font-size:18px;line-height:24px;text-transform:uppercase}
.area .chev{position:absolute;left:117px;top:201px}
.area-active{background:linear-gradient(160deg,#7a2a07,#a94a10);color:var(--white)}
.area-active .area-label{top:131px;font-size:17px;line-height:20px}

/* about */
.section-title{width:1200px;text-align:center;font-weight:300;font-size:33px;text-transform:uppercase;color:var(--ink)}
.about-title{left:-3px;top:898px}
.about-copy{left:225px;top:961px;width:750px;text-align:center;font-size:17px;line-height:21.5px;color:#333}
.about-copy p+p{margin-top:21px}
.about-btn{left:511px;top:1127px;width:177px;height:49px}

/* attorneys */
.attorneys{left:0;top:1170px;width:1200px;height:522px}
.att-title{left:13px;top:1318px;color:var(--white)}
.attorney-photo{width:174px;height:174px;border-radius:50%}
.att-name{font-size:18px;font-weight:700;color:var(--white);text-transform:uppercase}
.att-bio{font-family:"Lato",sans-serif;font-size:13.6px;line-height:23px;color:#f3e6de;width:290px}
.btn-outline{display:flex;align-items:center;justify-content:center;width:127px;height:36px;border:1.5px solid var(--white);color:var(--white);font-size:13px;font-weight:700;text-transform:uppercase}

/* blogs */
.blog-title{left:6px;top:1749px}
.blog-image{left:147px;top:1834px;width:434px;height:279px;background:linear-gradient(135deg,#c9d6e6,#8aa6c9 55%,#e6e2df)}
.blog-heading{left:621px;top:1827px;width:380px;font-size:22px;line-height:29px;color:#222;font-weight:400}
.blog-text{left:620px;top:1904px;width:420px;font-size:16.5px;line-height:24.7px;color:#666}
.blog-btn{left:620px;top:2050px;width:177px;height:48px}

/* contact */
.map{left:0;top:2226px;width:1200px;height:440px;background:linear-gradient(180deg,#e4e5e7,#d9dadd);border-top:1px solid #c9c9c9;border-bottom:1px solid #c9c9c9}
.contact-frame{left:378px;top:2303px;width:440px;height:262px;border:1px solid rgba(255,255,255,.9)}
.contact-card{left:388px;top:2312px;width:419px;height:243px;background:var(--white);text-align:center}
.contact-card h2{font-weight:400;font-size:28px;margin-top:32px;text-transform:uppercase}
.contact-card p{font-size:17px;line-height:32px}
.contact-card .lines{margin-top:8px}

/* footer */
.footer-nav{left:142px;top:2717px;display:flex;gap:33px;font-size:17px;font-weight:600;text-transform:uppercase}
.copyright{left:142px;top:2752px;font-size:12.5px;color:#222}
.social{top:2716px;width:22px;height:22px;border-radius:50%;border:2.5px solid var(--rust)}
</style>
</head>
<body>

<header class="site-header">
  <div class="abs brand">
    <div class="brand-name">Meridale Crown<br>Legal Group</div>
    <div class="brand-tag">Divorce and Personal Injury Lawyer</div>
  </div>
  <nav class="abs main-nav">
    <a href="#">Practice Areas</a><a href="#">Attorneys</a><a href="#">Blogs</a><a href="#">Contact Us</a>
  </nav>
  <div class="abs phone">
    <svg width="18" height="18" viewBox="0 0 24 24"><path fill="#a4450e" d="M6.6 10.8a15.1 15.1 0 0 0 6.6 6.6l2.2-2.2c.3-.3.7-.4 1-.2 1.1.4 2.3.6 3.6.6.6 0 1 .4 1 1V20c0 .6-.4 1-1 1A17 17 0 0 1 3 4c0-.6.4-1 1-1h3.5c.6 0 1 .4 1 1 0 1.3.2 2.5.6 3.6.1.3 0 .7-.2 1z"/></svg>
    1.808.555.0142
  </div>
</header>

<section class="abs hero" role="img" aria-label="Night view of a Hawaiian beachfront city skyline with a volcanic crater and bay"></section>
<h1 class="abs hero-title">Dedicated to making sure<br>you receive the care and<br>attention you need</h1>
<a class="abs btn hero-btn" href="#">Read More</a>
<div class="abs slider-dots"><span></span><span></span><span></span><span></span></div>

<svg class="abs about-bg" width="1200" height="650" viewBox="0 0 1200 650">
  <defs><linearGradient id="greyFade" x1="0" y1="0" x2="0" y2="1"><stop offset="0" stop-color="#dcdcdc"/><stop offset=".65" stop-color="#f5f5f5"/><stop offset="1" stop-color="#fff"/></linearGradient></defs>
  <path d="M0 105 Q600 -10 1200 80 L1200 650 L0 650 Z" fill="url(#greyFade)"/>
</svg>

<!-- practice areas -->
<div class="abs area" style="left:120px;top:560px">
  <svg class="icon" width="80" height="68" viewBox="0 0 80 68" fill="none" stroke="#a4450e" stroke-width="2.2">
    <circle cx="24" cy="12" r="8"/><circle cx="54" cy="12" r="8"/><circle cx="40" cy="40" r="6"/>
    <path d="M8 64V38c0-8 7-14 16-14s13 5 14 10M72 64V38c0-8-7-14-18-14-8 0-13 5-14 10M30 64V56c0-5 4-8 10-8s10 3 10 8v8"/>
  </svg>
  <div class="area-label">Family &amp;<br>Divorce</div>
  <svg class="chev" width="36" height="36" viewBox="0 0 36 36" fill="none" stroke="#555" stroke-width="1.6"><circle cx="18" cy="18" r="17"/><path d="M12 15l6 6 6-6"/></svg>
</div>
<div class="abs area" style="left:341px;top:560px">
  <svg class="icon" width="72" height="68" viewBox="0 0 72 68" fill="none" stroke="#a4450e" stroke-width="2.2">
    <circle cx="16" cy="12" r="7"/><path d="M22 20l14 14-8 12M36 34l12-8M20 22L8 40"/>
    <path d="M52 4h16v14c0 8-8 12-8 12s-8-4-8-12z"/><path d="M4 64h30l-4-12H10z"/>
  </svg>
  <div class="area-label">Personal<br>Injury</div>
  <svg class="chev" width="36" height="36" viewBox="0 0 36 36" fill="none" stroke="#555" stroke-width="1.6"><circle cx="18" cy="18" r="17"/><path d="M12 15l6 6 6-6"/></svg>
</div>
<div class="abs area" style="left:810px;top:560px">
  <svg class="icon" width="70" height="64" viewBox="0 0 70 64" fill="none" stroke="#a4450e" stroke-width="2.2">
    <path d="M6 30L34 6l28 24M14 24v14M48 10h8v12"/><path d="M4 60h26l16-10c4-2 2-8-3-6l-13 6H22"/><path d="M30 44l8-4"/>
  </svg>
  <div class="area-label">Real Estate</div>
  <svg class="chev" width="36" height="36" viewBox="0 0 36 36" fill="none" stroke="#555" stroke-width="1.6"><circle cx="18" cy="18" r="17"/><path d="M12 15l6 6 6-6"/></svg>
</div>
<div class="abs area area-active" style="left:585px;top:560px">
  <svg class="icon" width="78" height="60" viewBox="0 0 78 60" fill="none" stroke="#fff" stroke-width="2.2">
    <rect x="22" y="6" width="34" height="52"/><path d="M30 2h18v4"/>
    <path d="M28 14h4M37 14h4M46 14h4M28 22h4M37 22h4M46 22h4M28 30h4M37 30h4M46 30h4M28 38h4M37 38h4M46 38h4M35 58V48h8v10"/>
    <path d="M4 58h70M10 58V44M6 48h8M68 58V44M64 48h8"/>
  </svg>
  <div class="area-label">Corporate &amp;<br>Intellectual<br>Property</div>
  <svg class="chev" width="36" height="36" viewBox="0 0 36 36" fill="none" stroke="#fff" stroke-width="1.8"><circle cx="18" cy="18" r="17"/><path d="M12 15l6 6 6-6"/></svg>
</div>

<!-- about -->
<h2 class="abs section-title about-title">About the Kona Lawyers of MCLG</h2>
<div class="abs about-copy">
  <p>The experienced attorneys in the Meridale Crown Legal Group's Kailua Kona, Hawaii office provide clients with a wide range of litigation expertise, including legal claims involving divorce &amp; family, personal injury, toxic exposures, intellectual property, and real estate.</p>
  <p>Our Kona office also offers commercial and hospitality litigation expertise on behalf of a wide variety of clients, including restaurants, hotels, property owners, and many others.</p>
</div>
<a class="abs btn about-btn" href="#">Read More</a>

<!-- attorneys -->
<svg class="abs attorneys" width="1200" height="522" viewBox="0 0 1200 522" role="img" aria-label="Warm sunset over a Hawaiian coastline tinted in rust tones">
  <defs><linearGradient id="rustBand" x1="0" y1="0" x2="0" y2="1"><stop offset="0" stop-color="#8e300a"/><stop offset=".5" stop-color="#7a2a08"/><stop offset="1" stop-color="#9b3e12"/></linearGradient></defs>
  <path d="M0 8 Q600 170 1200 16 L1200 522 L0 522 Z" fill="url(#rustBand)"/>
</svg>
<h2 class="abs section-title att-title">Our Attorneys</h2>

<div class="abs attorney-photo" style="left:118px;top:1387px;background:radial-gradient(circle at 50% 45%,#b08b73,#2b2f4a 70%)" role="img" aria-label="Portrait of attorney Darren Velasko"></div>
<h3 class="abs att-name" style="left:308px;top:1400px">Darren Velasko, Esq</h3>
<p class="abs att-bio" style="left:308px;top:1430px">Darren Velasko graduated from Halecrest University, Pemberton College of Law, in 1972. He graduated magna cum laude from Ardmoor University College of Law</p>
<a class="abs btn-outline" href="#" style="left:308px;top:1540px">Read More</a>

<div class="abs attorney-photo" style="left:622px;top:1387px;background:radial-gradient(circle at 50% 45%,#c39a80,#8a9aa8 70%)" role="img" aria-label="Portrait of attorney Thomas Brevard"></div>
<h3 class="abs att-name" style="left:812px;top:1400px">Thomas Brevard, Esq.</h3>
<p class="abs att-bio" style="left:812px;top:1430px">Thomas Brevard graduated from Halecrest University, Pemberton College of Law, in 1971. He has over 35 years of experience as a litigator in both State</p>
<a class="abs btn-outline" href="#" style="left:813px;top:1542px">Read More</a>

<!-- blogs -->
<h2 class="abs section-title blog-title">Our Blogs</h2>
<svg class="abs" style="left:82px;top:1930px" width="30" height="52" viewBox="0 0 30 52" fill="none" stroke="#555" stroke-width="2"><path d="M26 2L4 26l22 24"/></svg>
<div class="abs blog-image" role="img" aria-label="Lawyer consulting with an injured client wearing a neck brace"></div>
<h3 class="abs blog-heading">Auscipit leo massa sodales velit et scelerisqmi tortor at ipsum Proin</h3>
<p class="abs blog-text">suscipit leo massa sodales velit et scelerisque mi tortor at ipsum Proin orci odio commodo ac gravida non tristique vel tellus Pellentesque nibh libero ultricies eu sagittis non mollis sed justo Praesent metus ipsum pulvinar pulvinar porta id fringilla at est</p>
<a class="abs btn blog-btn" href="#">Read More</a>
<svg class="abs" style="left:1071px;top:1930px" width="30" height="52" viewBox="0 0 30 52" fill="none" stroke="#555" stroke-width="2"><path d="M4 2l22 24L4 50"/></svg>

<!-- contact -->
<div class="abs map" role="img" aria-label="Street map of Kailua Kona showing the office location"></div>
<div class="abs contact-frame"></div>
<div class="abs contact-card">
  <h2>Contact Us</h2>
  <div class="lines">
    <p>74-2210 Halewai Road, Suite 318</p>
    <p>Kailua Kona, Hawaii 96740.</p>
    <p>+1.808.555.0142</p>
    <p>clients@tuvellattorney.com</p>
  </div>
</div>

<!-- footer -->
<nav class="abs footer-nav">
  <a href="#">Home</a><a href="#">Practice Areas</a><a href="#">Attorneys</a><a href="#">Blogs</a><a href="#">Contact Us</a>
</nav>
<div class="abs copyright">© 2019 Company Name &nbsp;All right reserved</div>
<span class="abs social" style="left:925px" aria-label="Social link"></span>
<span class="abs social" style="left:983px" aria-label="Social link"></span>
<span class="abs social" style="left:1042px" aria-label="Social link"></span>

</body>
</html>
```